Logo and Double sided business card

We need a logo and business card for a Point of Sale Business, Website is www.kestreltill.com.au - this is being worked on at the moment. There is a logo on the website - but this is more of a placement /logo and needs to be redesigned.
The address for Details for the Business card are

Person Name
KESTREL TILL
17/3 Worrigal Pde
Birchwood Vale 2167
Ph 1300 585 926 (1300 KTL 926)
Email : Person@kestreltill.com.au
Web: www.kestreltill.com.au

Our company will be a Point of Sale installation and Support business. We Specialise in the Vandrel Quill system.

We do
Installation of POS Systems
Support and Maintenance of existing POS
Quill POS support
Updates

Target Market(s)

Restaurants, hotels, retail shops

Industry/Entity Type

Business

Contact Information for Business Card

Person Name
KESTREL TILL
17/3 Worrigal Pde
Birchwood Vale 2167
Web: www.kestreltill.com.au

Logo Text

Kestrel Till

Font styles to use
Serif

Requirements
Must have
• We must have the source graphics in editable formats for both logo and business card.

```html
<!DOCTYPE html>
<html lang="en">
<head>
<meta charset="utf-8">
<title>Kestrel Till – Business Card</title>
<link rel="stylesheet" href="https://fonts.googleapis.com/css2?family=PT+Sans:wght@400;700&display=swap">
<style>
  :root {
    --backdrop: #3a3128;
    --card: #0b0b0b;
    --card-edge: #1c1c1c;
    --gold: #d8aa3e;
    --ink: #f2f2f2;
  }
  * { margin: 0; padding: 0; box-sizing: border-box; }
  html, body { width: 1200px; height: 858px; overflow: hidden; }
  body {
    background: var(--backdrop);
    font-family: "PT Sans", Arial, sans-serif;
    position: relative;
  }
  .card {
    position: absolute;
    top: 274px;
    width: 540px;
    height: 310px;
    background: linear-gradient(160deg, #151515 0%, var(--card) 55%, #050505 100%);
    border: 1px solid var(--card-edge);
    box-shadow: 0 14px 30px rgba(0,0,0,.45);
    overflow: hidden;
  }
  .card--front { left: 40px; }
  .card--back { left: 620px; }

  /* front */
  .brand {
    position: absolute;
    left: 40px;
    top: 70px;
    display: flex;
    align-items: center;
    gap: 14px;
  }
  .brand__mark {
    width: 34px; height: 34px;
    background: var(--gold);
  }
  .brand__name {
    color: var(--gold);
    font-size: 34px;
    font-weight: 400;
    letter-spacing: .5px;
    white-space: nowrap;
  }
  .holder {
    position: absolute;
    right: 232px;
    top: 148px;
    text-align: right;
  }
  .holder__name {
    color: var(--gold);
    font-size: 24px;
    line-height: 1.1;
    margin-bottom: 6px;
    white-space: nowrap;
  }
  .holder__address {
    color: var(--ink);
    font-size: 14px;
    line-height: 1.35;
    white-space: nowrap;
  }
  .divider {
    position: absolute;
    left: 322px;
    top: 140px;
    width: 2px;
    height: 104px;
    background: var(--gold);
  }
  .contact {
    position: absolute;
    left: 338px;
    top: 146px;
    list-style: none;
  }
  .contact__item {
    display: flex;
    align-items: center;
    gap: 8px;
    color: var(--ink);
    font-size: 12.5px;
    height: 26px;
    white-space: nowrap;
  }
  .contact__icon {
    width: 18px; height: 18px;
    flex: none;
  }

  /* back */
  .brand--back {
    left: 50%;
    top: 50%;
    transform: translate(-50%, -50%);
    gap: 18px;
  }
  .brand--back .brand__mark { width: 44px; height: 44px; }
  .brand--back .brand__name { font-size: 46px; }
</style>
</head>
<body>
  <section class="card card--front" aria-label="Business card front">
    <div class="brand">
      <span class="brand__mark"></span>
      <span class="brand__name">Kestrel Till</span>
    </div>

    <div class="holder">
      <p class="holder__name">Dana Holloway</p>
      <p class="holder__address">17/3 Worrigal Pde<br>Birchwood Vale 2167</p>
    </div>

    <span class="divider"></span>

    <ul class="contact">
      <li class="contact__item">
        <svg class="contact__icon" viewBox="0 0 18 18" aria-hidden="true">
          <rect width="18" height="18" rx="3" fill="#d8aa3e"/>
          <path d="M5 4.5h2.2l1 2.6-1.3.9a6 6 0 0 0 3.1 3.1l.9-1.3 2.6 1v2.2c0 .6-.5 1-1 1A8.5 8.5 0 0 1 4 5.5c0-.5.4-1 1-1z" fill="#0b0b0b"/>
        </svg>
        <span>1300 585 926 (1300 KTL 926)</span>
      </li>
      <li class="contact__item">
        <svg class="contact__icon" viewBox="0 0 18 18" aria-hidden="true">
          <rect width="18" height="18" rx="3" fill="#d8aa3e"/>
          <rect x="3.5" y="5" width="11" height="8" fill="#0b0b0b"/>
          <path d="M3.8 5.3 9 9.5l5.2-4.2" fill="none" stroke="#d8aa3e" stroke-width="1"/>
        </svg>
        <span>Person@kestreltill.com.au</span>
      </li>
      <li class="contact__item">
        <svg class="contact__icon" viewBox="0 0 18 18" aria-hidden="true">
          <rect width="18" height="18" rx="3" fill="#d8aa3e"/>
          <circle cx="9" cy="9" r="5" fill="none" stroke="#0b0b0b" stroke-width="1.3"/>
          <ellipse cx="9" cy="9" rx="2.2" ry="5" fill="none" stroke="#0b0b0b" stroke-width="1.1"/>
          <path d="M4 9h10" stroke="#0b0b0b" stroke-width="1.1"/>
        </svg>
        <span>www.kestreltill.com.au</span>
      </li>
    </ul>
  </section>

  <section class="card card--back" aria-label="Business card back">
    <div class="brand brand--back">
      <span class="brand__mark"></span>
      <span class="brand__name">Kestrel Till</span>
    </div>
  </section>
</body>
</html>
```